Harborline Motors LLC

Car Dealer Customer Service
Address: 2741 Linden Avenue, Shelbyville, TN 37162
web: www.harborlinemotorstn.net
email: harborlinemotorstn@mailbox-example.net
Phone: (931) 555-0148
Phone: (629) 555-0173

```html
<!DOCTYPE html>
<html lang="en">
<head>
<meta charset="utf-8">
<title>Harborline Motors – Business Card</title>
<link rel="stylesheet" href="https://fonts.googleapis.com/css2?family=Montserrat:wght@400;600;700&display=swap">
<style>
  :root {
    --brand-blue: #1b76a3;
    --accent-gold: #edb446;
    --ink: #3d3d3d;
    --card-white: #ffffff;
    --backdrop: #e6e7e9;
  }
  * { margin: 0; padding: 0; box-sizing: border-box; }
  html, body { width: 1054px; height: 1200px; overflow: hidden; }
  body {
    background: var(--backdrop);
    font-family: "Montserrat", sans-serif;
    position: relative;
  }
  .card {
    position: absolute;
    left: 72px;
    width: 910px;
    height: 519px;
    overflow: hidden;
  }
  .card--front { top: 62px; background: var(--card-white); }
  .card--back { top: 626px; background: var(--brand-blue); }

  /* Front: brand block */
  .brand-block {
    position: absolute;
    left: 36px;
    top: 158px;
    width: 340px;
    text-align: center;
  }
  .brand-mark {
    display: block;
    width: 150px;
    height: 150px;
    margin: 0 auto 22px;
    border-radius: 50%;
    background: var(--brand-blue);
  }
  .brand-name {
    font-weight: 700;
    font-size: 27px;
    letter-spacing: 0.3px;
    color: var(--brand-blue);
    white-space: nowrap;
  }

  .divider {
    position: absolute;
    left: 396px;
    top: 118px;
    width: 2px;
    height: 288px;
    background: var(--brand-blue);
  }

  /* Front: contact block */
  .contact-block {
    position: absolute;
    left: 416px;
    top: 108px;
    width: 462px;
    color: var(--ink);
  }
  .person-name {
    font-weight: 700;
    font-size: 44px;
    line-height: 1.05;
    color: var(--brand-blue);
    letter-spacing: 0.5px;
    white-space: nowrap;
  }
  .person-title {
    font-size: 25px;
    margin-top: 4px;
  }
  .contact-list { list-style: none; margin-top: 10px; }
  .contact-item {
    display: flex;
    align-items: center;
    gap: 12px;
    font-size: 19px;
    height: 32px;
    white-space: nowrap;
  }
  .contact-icon { width: 22px; height: 22px; flex: none; fill: var(--brand-blue); }
  .address {
    font-style: normal;
    font-size: 22px;
    line-height: 34px;
    margin-top: 12px;
    padding-left: 4px;
  }

  /* Front: footer stripes */
  .stripe-gold {
    position: absolute;
    left: 0; top: 493px;
    width: 518px; height: 12px;
    background: var(--accent-gold);
  }
  .stripe-blue {
    position: absolute;
    left: 0; top: 508px;
    width: 910px; height: 11px;
    background: var(--brand-blue);
  }
  .service-tab {
    position: absolute;
    right: 0; top: 481px;
    width: 368px; height: 38px;
    background: var(--brand-blue);
    clip-path: polygon(38px 0, 100% 0, 100% 100%, 0 100%);
    color: var(--card-white);
    font-weight: 700;
    font-size: 21px;
    line-height: 40px;
    text-align: right;
    padding-right: 14px;
  }

  /* Back */
  .back-brand {
    position: absolute;
    left: 0; right: 0;
    top: 130px;
    text-align: center;
  }
  .back-brand .brand-mark {
    width: 196px;
    height: 196px;
    margin-bottom: 30px;
    background: var(--card-white);
  }
  .back-brand .brand-name {
    font-size: 46px;
    color: var(--card-white);
  }
</style>
</head>
<body>

<section class="card card--front" aria-label="Business card front">
  <div class="brand-block">
    <span class="brand-mark" aria-hidden="true"></span>
    <p class="brand-name">HARBORLINE MOTORS</p>
  </div>

  <div class="divider"></div>

  <div class="contact-block">
    <h1 class="person-name">MARCUS ELLERY</h1>
    <p class="person-title">Managing Director</p>
    <ul class="contact-list">
      <li class="contact-item">
        <svg class="contact-icon" viewBox="0 0 24 24" aria-hidden="true"><path d="M6.6 10.8a15.2 15.2 0 0 0 6.6 6.6l2.2-2.2c.3-.3.7-.4 1-.2 1.1.4 2.3.6 3.6.6.6 0 1 .4 1 1V20c0 .6-.4 1-1 1A17 17 0 0 1 3 4c0-.6.4-1 1-1h3.5c.6 0 1 .4 1 1 0 1.2.2 2.4.6 3.6.1.3 0 .7-.2 1z"/></svg>
        (931) 555-0148
      </li>
      <li class="contact-item">
        <svg class="contact-icon" viewBox="0 0 24 24" aria-hidden="true"><path d="M6.6 10.8a15.2 15.2 0 0 0 6.6 6.6l2.2-2.2c.3-.3.7-.4 1-.2 1.1.4 2.3.6 3.6.6.6 0 1 .4 1 1V20c0 .6-.4 1-1 1A17 17 0 0 1 3 4c0-.6.4-1 1-1h3.5c.6 0 1 .4 1 1 0 1.2.2 2.4.6 3.6.1.3 0 .7-.2 1z"/></svg>
        (629) 555-0173
      </li>
      <li class="contact-item">
        <svg class="contact-icon" viewBox="0 0 24 24" aria-hidden="true"><path d="M2 5h20v14H2zm2 2v.4l8 5.3 8-5.3V7zm0 2.8V17h16V9.8l-8 5.3z"/></svg>
        harborlinemotorstn@mailbox-example.net
      </li>
      <li class="contact-item">
        <svg class="contact-icon" viewBox="0 0 24 24" aria-hidden="true"><circle cx="12" cy="12" r="10" fill="none" stroke="#1b76a3" stroke-width="2"/><path d="M12 2c3 3 3 17 0 20M12 2c-3 3-3 17 0 20M2 12h20" fill="none" stroke="#1b76a3" stroke-width="1.6"/></svg>
        www.harborlinemotorstn.net
      </li>
    </ul>
    <address class="address">2741 Linden Avenue,<br>Shelbyville, TN 37162</address>
  </div>

  <div class="stripe-gold"></div>
  <div class="stripe-blue"></div>
  <div class="service-tab">Car Dealer Customer Service</div>
</section>

<section class="card card--back" aria-label="Business card back">
  <div class="back-brand">
    <span class="brand-mark" aria-hidden="true"></span>
    <p class="brand-name">HARBORLINE MOTORS</p>
  </div>
</section>

</body>
</html>
```